Innovative Australian Importation company in Sustainability space needs beautiful website*

We seek your services to provide a clean, modern we rendered logo for or company Ferntide Commerce Imports Pty Ltd, this will be used in all the usual places however you will aso build us our business cards and our website: ferntidecommerceimports.example

What we do:
We source innovative products that solve problems in the Aeroponics, Hydroponics, Horticultural, Organics and sustainability space. We source our product from all over the world however our cliant base is predominantly in Australia & New Zealand Region.
Our company's mission is to help retail businesses by providing high-quality products at a competitive price for everyday people to produce healthy sustainable consumables from home, making it easy for the end-user to become more self-sufficient with while remaining environmentally friendly.

Target Market(s)

Aeroponics, Hydroponics, Horticultural, Organics and sustainability space.

Industry/Entity Type

Wholesale

Contact Information for Business Card

We would like these to be very modern and glossy possibly an embosed logo or rounded edges, a little smaller than the traditional?

Logo Text

Ferntide Commerce Imports

Coding

Coded - Design and coding required

Number of Pages Required

1 page

Colors
0355a3

Requirements
Must have
• The websit is bit of a landing page that will provide some minor information on our imported products. and qualify resellers ( Our target Market) from retail clients (the end-user) and provide a private store and check out for our trade customers. (not for Reatil)
Abillity to set up a trade account (must have our approval befor being granted access to shop.)
the abillity to for OEM's and International wholsalers register intrest.
The abillity to register/inquire about our produtc lines for Retailer.
The abillity to provide the end-user a list of resellers.
The ability for promo video
Nice to have
• .
Should not have
• Logo high gloss, 3d rendered

```html
<!DOCTYPE html>
<html lang="en">
<head>
<meta charset="utf-8">
<title>Ferntide Commerce Imports</title>
<link rel="stylesheet" href="https://fonts.googleapis.com/css2?family=Poppins:wght@500;600;700&family=Roboto:wght@300;400;500;700&family=Merriweather:wght@400;700&display=swap">
<style>
:root{
  --blue:#0355a3;
  --blue-dark:#02417d;
  --ink:#111;
  --text:#555;
  --muted:#888;
  --line:#ddd;
  --grey-bg:#f4f4f4;
  --footer:#262626;
  --footer-dark:#111;
  --white:#fff;
}
*{box-sizing:border-box;margin:0;padding:0}
html,body{width:1200px;height:4506px;overflow:hidden}
body{position:relative;font-family:"Roboto",sans-serif;color:var(--text);background:var(--white)}
.abs{position:absolute}
h2.section-title{position:absolute;left:0;width:1200px;text-align:center;font-family:"Poppins",sans-serif;font-weight:700;font-size:31px;letter-spacing:1px;color:var(--ink)}

/* top bar */
.topbar{top:0;left:0;width:1200px;height:32px;background:#f2f2f2;border-bottom:1px solid var(--line)}
.topbar p{position:absolute;left:78px;top:9px;font-size:11.5px;color:#666}
.topbar .social{position:absolute;right:90px;top:10px;display:flex;gap:14px}
.social span{width:11px;height:11px;border-radius:50%;background:#777;display:block}

/* header */
.header{top:32px;left:0;width:1200px;height:90px}
.brand{position:absolute;left:76px;top:36px;font-family:"Poppins",sans-serif;font-weight:600;font-size:19px;color:var(--blue)}
.contact-item{position:absolute;top:30px;display:flex;gap:14px}
.contact-item b{display:block;font-size:13px;font-weight:500;color:#222}
.contact-item small{display:block;font-size:11.5px;color:#888;margin-top:6px}
.btn{display:inline-block;background:var(--blue);color:var(--white);font-family:"Poppins",sans-serif;font-weight:500;border-radius:30px;text-align:center}
.btn-contact{position:absolute;left:969px;top:29px;width:126px;height:41px;line-height:41px;font-size:13px}

/* nav */
.nav{top:122px;left:0;width:1200px;height:55px;border-top:1px solid var(--line);border-bottom:1px solid var(--line)}
.nav ul{list-style:none;display:flex;position:absolute;left:75px;top:0;height:54px;border-left:1px solid var(--line)}
.nav li{padding:0 20px;line-height:54px;font-size:13px;color:#333;border-right:1px solid var(--line)}
.nav .tools{position:absolute;left:1025px;top:15px;display:flex;gap:12px;align-items:center}

/* hero */
.hero{top:177px;left:0;width:1200px;height:535px;background:linear-gradient(160deg,#6a5a3e 0%,#5b7a36 40%,#3f6a25 70%,#7a6a4a 100%)}
.hero-copy{position:absolute;left:0;top:185px;width:1200px;text-align:center;color:var(--white)}
.hero-copy h1{font-family:"Merriweather",serif;font-weight:400;font-size:37px}
.hero-copy p{font-size:21px;line-height:33px;margin-top:8px;color:#eee;font-weight:300}
.btn-hero{margin-top:18px;width:134px;height:43px;line-height:43px;font-size:12px}
.hero .arrow{position:absolute;top:255px}

.feature{top:586px;height:214px;width:218px;background:var(--blue);color:var(--white);text-align:center;display:flex;flex-direction:column;justify-content:center;align-items:center}
.feature h3{font-family:"Poppins",sans-serif;font-weight:600;font-size:17px}
.feature p{font-size:11.5px;line-height:21px;margin-top:12px}

/* about */
.about-title{left:126px;top:936px;font-family:"Poppins",sans-serif;font-weight:700;font-size:29px;letter-spacing:1px;color:var(--ink)}
.about-sub{left:126px;top:990px;font-size:12px;font-weight:500;color:var(--blue)}
.about-text{left:124px;top:1026px;width:512px;font-size:11px;line-height:21px;color:#888}
.btn-about{position:absolute;left:114px;top:1162px;width:118px;height:36px;line-height:36px;font-size:11px}
.about-img{left:654px;top:925px;width:446px;height:296px;background:linear-gradient(180deg,#cfd9e0 0%,#8fa86a 45%,#4b7a2a 70%,#6a5030 100%)}
.to-top{left:1148px;top:1183px;width:35px;height:35px;background:#999}

/* what we do */
.wwd-sub{left:300px;top:1356px;width:600px;text-align:center;font-size:12px;line-height:18px;font-weight:500;color:var(--blue)}
.service{top:1453px;width:321px;height:319px;border:3px solid var(--blue);border-top:none;text-align:center}
.service .cap{height:67px;background:var(--blue);position:relative}
.service .badge{position:absolute;left:113px;top:22px;width:90px;height:90px;border-radius:50%;background:var(--blue);display:flex;align-items:center;justify-content:center}
.service h3{margin-top:74px;font-family:"Merriweather",serif;font-weight:400;font-size:15px;color:#222;letter-spacing:1px}
.service p{margin:18px auto 0;width:270px;font-size:13px;line-height:20px;color:#333}
.service a{display:block;margin-top:30px;font-size:10px;font-weight:700;color:var(--blue);text-decoration:none}

/* stats */
.stats{top:1810px;left:0;width:1200px;height:338px;background:radial-gradient(circle at 48% 65%,#3f6e2a 0%,#2c4a1c 40%,#15230f 80%)}
.stat{top:1929px;width:237px;height:102px;border:1px solid rgba(255,255,255,.75);text-align:center;color:var(--white)}
.stat b{display:block;font-family:"Roboto",sans-serif;font-weight:500;font-size:57px;line-height:62px;margin-top:6px}
.stat span{display:block;font-family:"Merriweather",serif;font-weight:700;font-size:15px;margin-top:2px}

/* why */
.why-img-back{left:0;top:2309px;width:422px;height:260px;background:linear-gradient(180deg,#c8d2dc 0%,#8e9aa8 55%,#5b4f48 100%);box-shadow:0 3px 8px rgba(0,0,0,.25)}
.why-img-front{left:153px;top:2376px;width:295px;height:226px;background:linear-gradient(90deg,#4e7f2a 0%,#dfe5e2 45%,#6c9a38 100%)}
.play{left:256px;top:2480px}
.why-copy{left:479px;top:2322px;width:660px;font-size:11.5px;line-height:23px;color:#888}
.why-copy h4{font-size:16px;font-weight:500;color:var(--blue);margin-top:14px;line-height:24px}
.read-more{left:492px;top:2592px;font-size:19px;color:#333;letter-spacing:1px;border-bottom:3px solid var(--blue);padding-bottom:4px}

/* news */
.news-bg{top:2671px;left:0;width:1200px;height:468px;background:var(--grey-bg)}
.news{top:2809px;height:281px;border-radius:8px;color:var(--white);padding:112px 0 0 114px}
.news h3{font-family:"Poppins",sans-serif;font-weight:600;font-size:17px;line-height:18px;width:290px}
.news p{font-size:11px;line-height:23px;margin-top:14px;width:380px}

/* testimonials */
.testi{top:3293px;left:94px;width:1015px;height:338px;border:1px solid var(--blue);display:flex}
.quote{width:338px;border-right:1px solid var(--blue);text-align:center;position:relative}
.quote:last-child{border-right:none}
.quote .bar{position:absolute;left:8px;top:44px;width:320px;height:6px;background:var(--blue);transform:rotate(-2deg)}
.quote .avatar{position:absolute;left:125px;top:15px;width:88px;height:88px;border-radius:50%;border:3px solid var(--blue);background:linear-gradient(160deg,#8a6a5a,#c24a3a,#3c5f7a)}
.quote p{margin:126px auto 0;width:230px;font-size:14px;line-height:23px;color:#777}
.quote h5{font-size:20px;font-weight:400;color:var(--blue);margin-top:14px}
.quote small{display:block;font-size:11px;color:#aaa;margin-top:6px}
.stars{display:flex;gap:4px;justify-content:center;margin-top:20px}

/* contact map */
.map{top:3699px;left:0;width:1200px;height:420px;background:linear-gradient(135deg,#e8e6df 0%,#dfe5d8 50%,#e4e2dc 100%)}
.field{left:672px;width:355px;background:var(--white);border:1px solid #ccc;font-size:11px;font-style:italic;color:#557;padding:7px 8px}
.btn-send{left:672px;top:4055px;width:353px;height:28px;line-height:28px;background:var(--blue);color:var(--white);font-size:10px;font-weight:700;text-align:center}

/* footer */
.footer{top:4119px;left:0;width:1200px;height:301px;background:var(--footer);color:#bbb}
.footer h4{position:absolute;top:67px;font-family:"Poppins",sans-serif;font-weight:600;font-size:16px;color:var(--white);letter-spacing:.5px}
.footer p{position:absolute;font-size:12px;line-height:22px}
.footer ul{position:absolute;left:393px;top:114px;list-style:none;font-size:13px;color:var(--white)}
.footer li{line-height:35px}
.tags{position:absolute;left:554px;top:104px;width:290px;display:flex;flex-wrap:wrap;gap:9px 8px}
.tags span{background:var(--blue);color:var(--white);font-size:11.5px;font-weight:700;border-radius:20px;padding:0 20px;height:33px;line-height:33px}
.btn-signup{position:absolute;left:852px;top:186px;width:107px;height:35px;line-height:35px;border-radius:20px;background:var(--white);color:var(--blue);font-size:12px;text-align:center}
.footer .social{position:absolute;left:112px;top:190px;display:flex;gap:48px}
.footer .social span{background:#ddd}
.copyright{top:4420px;left:0;width:1200px;height:86px;background:var(--footer-dark);color:var(--white);text-align:center;font-size:12px;font-weight:700;line-height:86px}
</style>
</head>
<body>

<div class="abs topbar">
  <p>We offer landscaping , maintenance and design for residential, commercial and industrial clients</p>
  <div class="social"><span></span><span></span><span></span><span></span></div>
</div>

<header class="abs header">
  <div class="brand">Ferntide Commerce Imports</div>
  <div class="contact-item" style="left:427px">
    <svg width="24" height="24" viewBox="0 0 24 24"><path fill="#0355a3" d="M6.6 10.8a15 15 0 0 0 6.6 6.6l2.2-2.2a1 1 0 0 1 1-.25 11.4 11.4 0 0 0 3.6.57 1 1 0 0 1 1 1V20a1 1 0 0 1-1 1A17 17 0 0 1 3 4a1 1 0 0 1 1-1h3.5a1 1 0 0 1 1 1c0 1.25.2 2.45.57 3.57a1 1 0 0 1-.25 1z"/></svg>
    <div><b>+61 2 5550 1842</b><small>Mon-Fri, 8:30am - 6:30pm</small></div>
  </div>
  <div class="contact-item" style="left:670px">
    <svg width="24" height="20" viewBox="0 0 24 20"><rect x="1.5" y="1.5" width="21" height="17" rx="2" fill="none" stroke="#0355a3" stroke-width="2.2"/><path d="M2 3l10 8 10-8" fill="none" stroke="#0355a3" stroke-width="2.2"/></svg>
    <div><b>hello@ferntide.example</b><small>Mail Us</small></div>
  </div>
  <a class="btn btn-contact">Contact Us</a>
</header>

<nav class="abs nav">
  <ul><li>HOME</li><li>ABOUT</li><li>PAGES</li><li>ELEMENT</li><li>BLOG</li><li>CONTACT</li></ul>
  <div class="tools">
    <svg width="22" height="22" viewBox="0 0 22 22"><circle cx="9" cy="9" r="6.5" fill="none" stroke="#111" stroke-width="2.6"/><path d="M14 14l6 6" stroke="#111" stroke-width="3"/></svg>
    <span style="width:2px;height:26px;background:#111;display:block"></span>
    <svg width="26" height="22" viewBox="0 0 26 22"><path d="M1 3h4l3 11h13l3-8H7" fill="none" stroke="#111" stroke-width="1.6"/><circle cx="10" cy="18" r="1.6" fill="#111"/><circle cx="19" cy="18" r="1.6" fill="#111"/></svg>
  </div>
</nav>

<section class="abs hero" role="img" aria-label="Hand holding a fresh lettuce above rows of hydroponic greens">
  <svg class="arrow" style="left:20px" width="14" height="24" viewBox="0 0 14 24"><path d="M12 2L2 12l10 10" fill="none" stroke="#fff" stroke-width="2"/></svg>
  <svg class="arrow" style="left:1166px" width="14" height="24" viewBox="0 0 14 24"><path d="M2 2l10 10L2 22" fill="none" stroke="#fff" stroke-width="2"/></svg>
  <div class="hero-copy">
    <h1>Hydroponic</h1>
    <p>Trust The Greenway Crew professionals to take care of your<br>commercial or residential grounds.</p>
    <a class="btn btn-hero">LEARN MORE</a>
  </div>
</section>

<div class="abs feature" style="left:136px"><h3>HYDROPONIC</h3></div>
<div class="abs feature" style="left:374px">
  <svg width="46" height="36" viewBox="0 0 46 36"><path d="M3 12L23 2l20 10v22H3z" fill="#fff"/><rect x="11" y="16" width="24" height="3" fill="#0355a3"/><rect x="11" y="22" width="24" height="3" fill="#0355a3"/><rect x="11" y="28" width="24" height="3" fill="#0355a3"/></svg>
  <h3 style="margin-top:8px">AEROPONIC</h3>
  <p>Our Aeroponic Services Are<br>Best For Growing Plantation.</p>
</div>
<div class="abs feature" style="left:610px"><h3>HORTICULTURE</h3></div>
<div class="abs feature" style="left:847px"><h3>SUSTAINABILITY</h3></div>

<h2 class="abs about-title">FERNTIDE COMMERCE IMPORTS</h2>
<p class="abs about-sub">The Most Relaiable &amp; Professional Company for Gardening &amp; Lawncare Service</p>
<p class="abs about-text">Lorem ipsum dolor sit amet, consectetur adipiscing elit. Suspendisse suscipit, tortor porttitor gravida ultricies, sem nibh accumsan arcu, a lacinia dui tellus in urna. Mauris eu turpis ultrices, facilisis libero at, tristique quam. Etiam eu augue ut ipsum pharetra dapibus. Aliquam et hendrerit arcu. Aenean molestie vulputate imperdiet. Aenean ut dictum dolor, quis lobortis neque. Proin fermentum placerat odio vitae scelerisque. Mauris est quam, aliquam sit amet tempus a, tempus ac libero. Etiam massa odio, bibendum in risus eu, ultricies varius libero.</p>
<a class="btn btn-about">MORE ABOUT</a>
<div class="abs about-img" role="img" aria-label="Greenhouse tunnel with long rows of hydroponic plants"></div>
<div class="abs to-top"><svg width="35" height="35" viewBox="0 0 35 35"><path d="M12 20l5.5-6 5.5 6z" fill="#fff"/></svg></div>

<h2 class="section-title" style="top:1300px">WHAT WE DO</h2>
<p class="abs wwd-sub">We source innovative products that solve problems in the Aeroponics, Hydroponics, Horticultural,<br>Organics and sustainability space.</p>

<div class="abs service" style="left:101px">
  <div class="cap"><div class="badge"><svg width="40" height="40" viewBox="0 0 40 40"><path d="M4 20a16 14 0 0 1 32 0c-3-2-6-2-8 0-2-2-6-2-8 0-2-2-6-2-8 0-2-2-5-2-8 0z" fill="#fff"/><path d="M20 20v11a3 3 0 0 1-6 0" fill="none" stroke="#fff" stroke-width="2.5"/></svg></div></div>
  <h3>RELIABILITY</h3>
  <p>Lorem ipsum dolor sit amet, consectetur adipiscing elit. Cras diam purus, sagittis quis augue et, dictum rhoncus ante.</p>
  <a>Read More</a>
</div>
<div class="abs service" style="left:441px">
  <div class="cap"><div class="badge"><svg width="40" height="40" viewBox="0 0 40 40"><circle cx="20" cy="20" r="16" fill="none" stroke="#fff" stroke-width="3"/><path d="M16 30V11h6a5 5 0 0 1 0 10h-6" fill="none" stroke="#fff" stroke-width="3.5"/></svg></div></div>
  <h3>PRODUCTS</h3>
  <p>Lorem ipsum dolor sit amet, consectetur adipiscing elit. Cras diam purus, sagittis quis augue et, dictum rhoncus ante.</p>
  <a>Read More</a>
</div>
<div class="abs service" style="left:778px">
  <div class="cap"><div class="badge"><svg width="44" height="32" viewBox="0 0 44 32"><rect x="2" y="2" width="40" height="28" rx="3" fill="#fff"/><text x="7" y="22" font-family="Roboto,sans-serif" font-size="16" font-weight="700" fill="#0355a3">$</text><rect x="20" y="11" width="16" height="3" fill="#0355a3"/><rect x="20" y="18" width="16" height="3" fill="#0355a3"/></svg></div></div>
  <h3>PRICE</h3>
  <p>Lorem ipsum dolor sit amet, consectetur adipiscing elit. Cras diam purus, sagittis quis augue et, dictum rhoncus ante.</p>
  <a>Read More</a>
</div>

<section class="abs stats" role="img" aria-label="Hand holding a leafy green globe against a forest backdrop"></section>
<div class="abs stat" style="left:100px"><b>4,050</b><span>PROJECT DONE</span></div>
<div class="abs stat" style="left:355px"><b>1,230</b><span>PLANT TYPES</span></div>
<div class="abs stat" style="left:609px"><b>3,350</b><span>HAPPY CLIENTS</span></div>
<div class="abs stat" style="left:864px"><b>520</b><span>AWARDS</span></div>

<h2 class="section-title" style="top:2216px">WHY PEOPLE CHOOSE US</h2>
<div class="abs why-img-back" role="img" aria-label="Team working together in a city office"></div>
<div class="abs why-img-front" role="img" aria-label="Vertical aeroponic towers filled with leafy plants"></div>
<svg class="abs play" width="90" height="90" viewBox="0 0 90 90"><circle cx="45" cy="45" r="40" fill="rgba(255,255,255,.2)" stroke="#fff" stroke-width="3"/><path d="M37 29l22 16-22 16z" fill="#fff"/></svg>
<div class="abs why-copy">
  <p>Gorem ipsum dolor sit amet, consectetur adipiscing elitsed do eium od tempor incididunt. Gorem ipsum dolor sit amet, consectetur adipiscing elitsed.</p>
  <h4>MODERN EQUIPMENT:</h4>
  <p>Dorem ipsum dolor sit amet, consectetur adipiscing elitsed do eium od tempor incididunte Gorem ipsum dolor sit amet, consectetur adipiscing elitsed.</p>
  <h4>WHOLESALE:</h4>
  <p>Dorem ipsum dolor sit amet, consectetur adipiscing elitsed do eium od tempor incididunte.</p>
</div>
<div class="abs read-more">Read More</div>

<div class="abs news-bg"></div>
<h2 class="section-title" style="top:2727px">WHAT'S NEW THINGS</h2>
<article class="abs news" style="left:82px;width:509px;background:linear-gradient(180deg,#5c5a58 0%,#8a6a4a 60%,#6b4a2a 100%)" role="img" aria-label="Harvested wheat field at dusk">
  <h3>Summer Crop Nutrition and Fertilizer Requirements</h3>
  <p>Contrary to popular belief, Lorem Ipsum is not simply random text. It has roots in a piece of classical Latin</p>
</article>
<article class="abs news" style="left:603px;width:502px;background:linear-gradient(180deg,#8a8470 0%,#5d6a3a 55%,#3a4a22 100%)" role="img" aria-label="Rows of young corn growing in a field">
  <h3>Grow Your Farming Work Through Our Refresh Products</h3>
  <p>Contrary to popular belief, Lorem Ipsum is not simply random text. It has roots in a piece of classical Latin</p>
</article>

<h2 class="section-title" style="top:3222px">WHAT OUR CUSTOMER SAY</h2>
<div class="abs testi">
  <div class="quote"><div class="bar"></div><div class="avatar" role="img" aria-label="Customer portrait"></div>
    <p>Thanks for the awesome service! Waited fors than 30 mins to get my seed trays' are all super friendly!</p>
    <h5>Mara Ellison</h5><small>Northvale Limited</small>
    <div class="stars"><svg width="108" height="18" viewBox="0 0 108 18"><g fill="#f5a623"><path id="st" d="M9 1l2.4 5.3 5.6.6-4.2 3.8 1.2 5.6L9 13.4 4 16.3l1.2-5.6L1 6.9l5.6-.6z"/><use href="#st" x="22"/><use href="#st" x="44"/><use href="#st" x="66"/><use href="#st" x="88"/></g></svg></div>
  </div>
  <div class="quote"><div class="bar"></div><div class="avatar" role="img" aria-label="Customer portrait"></div>
    <p>Thanks for the awesome service! Waited fors than 30 mins to get my seed trays' are all super friendly!</p>
    <h5>Mara Ellison</h5><small>Northvale Limited</small>
    <div class="stars"><svg width="108" height="18" viewBox="0 0 108 18"><g fill="#f5a623"><use href="#st"/><use href="#st" x="22"/><use href="#st" x="44"/><use href="#st" x="66"/><use href="#st" x="88"/></g></svg></div>
  </div>
  <div class="quote"><div class="bar"></div><div class="avatar" role="img" aria-label="Customer portrait"></div>
    <p>Thanks for the awesome service! Waited fors than 30 mins to get my seed trays' are all super friendly!</p>
    <h5>Mara Ellison</h5><small>Northvale Limited</small>
    <div class="stars"><svg width="108" height="18" viewBox="0 0 108 18"><g fill="#f5a623"><use href="#st"/><use href="#st" x="22"/><use href="#st" x="44"/><use href="#st" x="66"/><use href="#st" x="88"/></g></svg></div>
  </div>
</div>

<section class="abs map" role="img" aria-label="Street map showing the office location"></section>
<div class="abs field" style="top:3720px;height:37px">Name</div>
<div class="abs field" style="top:3777px;height:37px">Email</div>
<div class="abs field" style="top:3832px;height:200px">Message</div>
<div class="abs btn-send">SEND</div>

<footer class="abs footer">
  <h4 style="left:110px">FERNTIDE COMMERCE IMPORTS</h4>
  <p style="left:110px;top:111px;width:260px">Praesent vel rutrum purus. Nam vel dui eu risus duis. Praesent vel rutrum purus. Nam vel dui eu risus duis</p>
  <div class="social"><span></span><span></span><span></span><span></span></div>
  <h4 style="left:393px">USEFUL LINKS</h4>
  <ul><li>Ordering Info</li><li>Shipping &amp; Delivery</li><li>Pricing Tables</li><li>Our Guarantee</li></ul>
  <h4 style="left:554px">TAG CLOUDS</h4>
  <div class="tags"><span>HYDROPONICS</span><span>ORGANIC</span><span>AEROPONICS</span><span>HORTICULTURAL</span><span>SUSTAINABILITY SPACE</span></div>
  <h4 style="left:852px">SignUp For Newsletter</h4>
  <p style="left:852px;top:111px;width:240px">We have environmentally friendly products.</p>
  <a class="btn-signup">&#8594; SIGNUP</a>
</footer>
<div class="abs copyright">© Copyright Leafhold 2018. Designed and Developed by</div>

</body>
</html>
```